Oil and gas industry project solutions company needs professional cards with Canadian aboriginal fee

We are a aboriginally owned company that is focused on Project Planning, Management, Inspection & Consulting for Canada's Petroleum Industry. We have a logo that we would like to incorporate into a professional looking business card. We are professionals that offer services from project inception to completion.

Target Market(s)

Major industry leaders like NorthRidge Pipelines, Vantor, Kelstrand Energy, Brimwell etc.

Industry/Entity Type

Industry

Contact Information for Business Card

Reid Forbin
reid@kolbymarsh.ca
250 418 9067

Requirements
Must have
• KolbyMarsh Inc. logo.
• Address is: RR4, Site2, Comp7 Fort St. John, BC V1J 8K3 Traditional Territory of the Treaty 8 People
• Colors that are in logo
• Banner or picture on back
• Ability to put different names and contacts
• Website: kolbymarsh.ca
• "Project Planning, Management, Inspection & Consulting for Canada's Petroleum Industry"

```html
<!DOCTYPE html>
<html lang="en">
<head>
<meta charset="utf-8">
<title>KolbyMarsh Inc. – Business Card</title>
<link rel="stylesheet" href="https://fonts.googleapis.com/css2?family=Cormorant+Garamond:ital,wght@1,600&family=Open+Sans:wght@400;700&display=swap">
<style>
  :root {
    --navy: #3b3e74;
    --navy-deep: #33366a;
    --green: #6fae4f;
    --grey-text: #4d4d4f;
    --dark-text: #333335;
    --rule: #8a8a8c;
    --paper: #ffffff;
    --backdrop: #e6e6e6;
    --photo-earth: #8a6a3e;
    --photo-snow: #5d6f86;
    --photo-site: #6a6448;
  }
  * { margin: 0; padding: 0; box-sizing: border-box; }
  html, body {
    width: 1200px; height: 406px; overflow: hidden;
    background: var(--backdrop);
    font-family: "Open Sans", Arial, sans-serif;
  }
  .card {
    position: absolute; top: 70px;
    width: 468px; height: 266px;
    box-shadow: 0 3px 10px rgba(0,0,0,.25);
  }
  .card--front { left: 122px; background: var(--paper); }
  .card--back { left: 633px; background: var(--navy); overflow: hidden; }

  .brand {
    position: absolute; left: 28px; top: 30px;
    display: flex; align-items: center; gap: 10px;
  }
  .brand__mark { width: 30px; height: 30px; border-radius: 50%; background: var(--green); }
  .brand__text { display: flex; flex-direction: column; align-items: center; }
  .brand__name {
    font-size: 25px; font-weight: 700; color: var(--navy);
    letter-spacing: -0.5px; line-height: 1;
  }
  .brand__suffix {
    display: flex; align-items: center; gap: 8px;
    font-size: 14px; font-weight: 700; color: var(--navy); margin-top: 3px;
  }
  .brand__suffix::before, .brand__suffix::after {
    content: ""; width: 50px; height: 1px; background: var(--rule);
  }

  .name-band {
    position: absolute; left: 248px; top: 46px; width: 220px; height: 32px;
    background: var(--navy); color: #fff;
    display: flex; align-items: center; padding-left: 12px; gap: 4px;
  }
  .name-band__name { font-family: "Cormorant Garamond", Georgia, serif; font-style: italic; font-weight: 600; font-size: 20px; }
  .name-band__phone { font-size: 13px; }

  .services, .address {
    position: absolute; left: 77px;
    font-size: 12.3px; line-height: 20px; color: var(--grey-text);
  }
  .services { top: 105px; }
  .address { top: 153px; }

  .contact-rule {
    position: absolute; left: 70px; top: 225px; width: 332px; height: 1px; background: var(--rule);
  }
  .contact {
    position: absolute; left: 76px; top: 234px;
    font-size: 11.8px; font-weight: 700; color: var(--dark-text);
  }

  .collage { position: absolute; left: 0; top: 0; }
</style>
</head>
<body>
  <section class="card card--front" aria-label="Card front">
    <div class="brand">
      <span class="brand__mark"></span>
      <div class="brand__text">
        <span class="brand__name">KolbyMarsh</span>
        <span class="brand__suffix">Inc.</span>
      </div>
    </div>
    <div class="name-band">
      <span class="name-band__name">Reid Forbin</span>
      <span class="name-band__phone">| 250 418 9067</span>
    </div>
    <p class="services">Project Planning | Management | Inspection &amp; Consulting<br>for Canada's Petroleum Industry</p>
    <p class="address">RR4, Site2, Comp7 Fort St. John, BC V1J 8K3<br>Traditional Territory of the Treaty 8 People</p>
    <div class="contact-rule"></div>
    <p class="contact">E -mail : reid@kolbymarsh.ca | &nbsp;Website : kolbymarsh.ca</p>
  </section>

  <section class="card card--back" aria-label="Card back">
    <svg class="collage" width="468" height="266" viewBox="0 0 468 266">
      <g transform="translate(216 130) rotate(-12.5)">
        <rect x="-185" y="-85" width="370" height="170" fill="#fff"/>
        <rect x="-180" y="-80" width="160" height="80" fill="var(--photo-earth)" role="img" aria-label="Photo: pipeline sections with yellow coating on a field site"/>
        <rect x="-16" y="-80" width="196" height="80" fill="var(--photo-snow)" role="img" aria-label="Photo: crew in safety vests lowering pipe into a snowy trench"/>
        <rect x="-180" y="4" width="360" height="76" fill="var(--photo-site)" role="img" aria-label="Photo: pipelayer machines on a construction right-of-way"/>
        <text x="183" y="104" text-anchor="end" fill="#fff" font-family="Open Sans, Arial, sans-serif" font-weight="700" font-size="13">kolbymarsh.ca</text>
      </g>
    </svg>
  </section>
</body>
</html>
```